Trifold Brochure

This is relatively easy. We already have a trifold made we simply want to update the LOOK to look more like our current website. All content would stay the same the only thing that would change would be the fonts, colors and background images to match the current website.

I have attached a word doc of the old trifold brochure. We would want the content to remain on the same pages of the trifold. Again all you are doing is updating the font, logo, colors and any background images. Please comment with any questions.

This is a 5 day project!

Requirements
Must have
• Logo, colors and fonts to match our current website.
http://www.brambleworksgroup.example/

```html
<!DOCTYPE html>
<html lang="en">
<head>
<meta charset="utf-8">
<title>Brambleworks Group – Trifold Brochure</title>
<link href="https://fonts.googleapis.com/css2?family=Open+Sans:wght@400;600;700;800&display=swap" rel="stylesheet">
<style>
  :root {
    --green-dark: #4a6220;
    --green-deep: #3f551b;
    --green-mid: #8fa85a;
    --green-light: #b9cc8c;
    --green-pale: #d9e4c2;
    --wood: #c8d49f;
    --wood-light: #e4dcb8;
    --ink: #2f2f2f;
    --paper: #ffffff;
    --stage: #dcdcdc;
  }
  * { box-sizing: border-box; margin: 0; padding: 0; }
  html, body { width: 1200px; height: 982px; overflow: hidden; }
  body {
    background: var(--stage);
    font-family: "Open Sans", Arial, sans-serif;
    color: var(--ink);
  }
  .brochure {
    position: absolute;
    left: 108px; top: 111px;
    width: 984px; height: 760px;
    display: flex;
    box-shadow: 0 6px 24px rgba(0,0,0,.18);
  }
  .panel {
    position: relative;
    width: 328px; height: 760px;
    background: var(--paper);
    overflow: hidden;
  }
  .panel + .panel { border-left: 1px solid #e6e6e6; }

  /* Headers */
  .band-top {
    background: var(--green-dark);
    color: #fff;
    font-weight: 700;
  }
  .cover-title {
    height: 160px;
    padding: 22px 26px 0 90px;
    font-size: 30px;
    line-height: 1.15;
    text-align: center;
  }
  .panel-title {
    height: 58px;
    padding-top: 18px;
    font-size: 15px;
    text-align: center;
  }

  /* Bottom bands */
  .band-bottom {
    position: absolute; left: 0; right: 0; bottom: 0;
    height: 78px;
    background: var(--green-dark);
  }
  .band-bottom .tab {
    position: absolute; top: 0; height: 22px;
  }
  .band-bottom .tab-a { left: 70px; width: 48px; background: var(--green-pale); }
  .band-bottom .tab-b { left: 118px; width: 80px; background: var(--green-light); }

  /* Who we are */
  .about { padding: 14px 24px 0; }
  .about h2 {
    font-size: 11px; font-weight: 700;
    text-align: center; letter-spacing: .5px;
    margin-bottom: 8px;
  }
  .about p {
    font-size: 8.6px; line-height: 1.5;
    text-align: justify; text-indent: 18px;
    margin-bottom: 10px;
  }

  /* Middle panel */
  .wood-strip {
    height: 34px;
    background: linear-gradient(180deg, var(--wood-light), var(--wood) 60%, #dfe7c7);
  }
  .grid-backdrop {
    position: absolute; left: 0; right: 0; top: 92px; height: 150px;
    background: linear-gradient(180deg, #f4f4f4, #fff);
  }
  .designer { position: relative; padding: 40px 24px 0; }
  .designer h3 { font-size: 9px; font-weight: 400; margin-bottom: 6px; }
  .designer h4 { font-size: 9px; font-weight: 400; margin-bottom: 6px; padding-left: 8px; }
  .designer p {
    font-size: 8.6px; line-height: 1.5;
    text-align: justify; text-indent: 18px;
    margin-bottom: 8px;
  }
  .contact {
    position: absolute; left: 0; right: 0; top: 520px;
    text-align: center; font-size: 9.5px; line-height: 1.55;
  }
  .contact a { color: var(--ink); }
  .wood-foot {
    position: absolute; left: 0; right: 0; bottom: 0; height: 64px;
    background: linear-gradient(180deg, var(--green-light), var(--wood) 40%, #b7c98a);
  }

  /* Brand mark (name + plain square) */
  .brand-mark {
    display: flex; align-items: center; justify-content: center; gap: 8px;
    color: var(--green-dark);
    font-weight: 700; font-size: 14px;
  }
  .brand-mark .square {
    width: 22px; height: 22px; background: var(--green-mid);
  }
  .contact .brand-mark { margin-bottom: 18px; }

  /* Cover panel */
  .side-strip {
    position: absolute; left: 0; top: 58px; bottom: 78px; width: 66px;
    background: var(--green-light);
  }
  .cover-backdrop {
    position: absolute; left: 66px; right: 0; top: 58px; height: 300px;
    background: linear-gradient(180deg, #eef0ee, #fff);
  }
  .cover-body { position: absolute; left: 66px; right: 0; top: 140px; text-align: center; }
  .slogan {
    margin-top: 40px;
    color: var(--green-dark);
    font-weight: 800; font-size: 21px; line-height: 1.2;
    letter-spacing: 1.5px;
  }
  .tagline {
    margin: 70px 20px 0 28px;
    text-align: left;
    color: var(--green-dark);
    font-weight: 700; font-size: 17px; line-height: 1.45;
  }
</style>
</head>
<body>
<main class="brochure">

  <section class="panel panel-about">
    <header class="band-top cover-title">Brambleworks Group, LLC</header>
    <div class="about">
      <h2>WHO WE ARE</h2>
      <p>Following the devastation of Hurricane Sandy, countless homes along the Northeast Coastline were dislodged from their piling foundations. Some of the pilings were completely destroyed while others subsided. Brambleworks Group, LLC (BWG) was established by a team of Engineers, Designers and Material Specialists that witnessed the destruction and aftermath personally. This highly skilled team provided engineering services to homeowners along the coast. During the initial stage of the aftermath recovery efforts at this time, the BWG team identified a need for an improved solution.</p>
      <p>Traditional options available on the market presented problems for the recovery of homes on pilings that needed to be repaired or raised. Options provided to homeowners had drawbacks. The traditional method includes lifting and moving the home away from the pilings, then drive new pilings, and then move the home back. This alternative presented several problems, such as cost and where to place the house during the installation of the pilings. Simply put there is no room for this option in most cases.</p>
      <p>As a result, BWG developed a system which allows the house to be raised without actually moving the home. The Collars are installed, and the house reset on the Collars without the expense of moving the house or driving new pilings. This option can be installed in a matter of days with limited space and at a lower construction cost. Please see our technical brief for a review of your options and how our system compares to other methods.</p>
    </div>
    <div class="band-bottom"><span class="tab tab-a"></span><span class="tab tab-b"></span></div>
  </section>

  <section class="panel panel-designer">
    <header class="band-top panel-title">Brambleworks Group, LLC</header>
    <div class="wood-strip"></div>
    <div class="grid-backdrop" role="img" aria-label="Faint architectural framing line drawing"></div>
    <div class="designer">
      <h3>Designer's Corner:</h3>
      <h4>Notes to Design Professionals:</h4>
      <p>We have a staff Engineer who can assist you with developing permit plans for submission for approval under Section 104.11 of the IRC. We can provide you with standard details in ACAD format with appropriate construction notes and detailed product specification for use in construction documents.</p>
      <p>When designing using our systems, be sure to understand that our system is simply an extension of the piling, and as such, standard lateral supporting must be considered.</p>
      <p>An inspection of each piling is required by the professional to ensure that the piling is free from alignment deflection of greater than 6 degrees, free from dry rot, damage or other defect.</p>
      <p>Our system can be installed below grade. If there is dry rot on the exposed surface of the pile, dig down into the sand; it is likely the piling below the sand and/or the water table is structurally sound. The BWG system can be used as a splice to remove failed sections of pilings and install new sections.</p>
    </div>
    <div class="contact">
      <div class="brand-mark"><span class="square"></span>Brambleworks Group</div>
      PO Box 4418, Fernbrook, PA 18900-0040<br>
      T. 555 014 2270 | F. 555 014 9831<br>
      <strong>Email:</strong> <a href="mailto:sales@brambleworksgroup.example">sales@brambleworksgroup.example</a><br>
      <a href="http://www.brambleworksgroup.example/">www.brambleworksgroup.example</a>
    </div>
    <div class="wood-foot"></div>
  </section>

  <section class="panel panel-cover">
    <header class="band-top panel-title">Brambleworks Group, LLC</header>
    <div class="cover-backdrop" role="img" aria-label="Faint architectural framing line drawing"></div>
    <div class="side-strip"></div>
    <div class="cover-body">
      <div class="brand-mark"><span class="square"></span>Brambleworks Group</div>
      <p class="slogan">REBUILD SAFER<br>STRONGER<br>BETTER</p>
      <p class="tagline">We provide piling repair systems to allow for cost effective reconstruction and modifications to structures on pilings</p>
    </div>
    <div class="band-bottom"><span class="tab tab-a"></span><span class="tab tab-b"></span></div>
  </section>

</main>
</body>
</html>
```